Sole trader requires buisness card / company logo for mining and aviation

I require a business card and logo design having the following requirements;
Skyward and Engine Works
Owner: Dorian Vecksley
Ph: 0471593064
E: dorian-r-vecksley@quillmail.com.au

Logo should include a basic aircraft image and an image of an item of mining machinery either a dump truck or large excavator, but keeping in mind that the image is to be transferred onto clothing embroidery.

```html
<!DOCTYPE html>
<html lang="en">
<head>
<meta charset="utf-8">
<title>Skyward and Engine Works – Business Card</title>
<link href="https://fonts.googleapis.com/css2?family=Ubuntu:wght@400;500&display=swap" rel="stylesheet">
<style>
  :root {
    --brand-purple: #4b2b8f;
    --card-light: #e9e8ec;
    --card-white: #ffffff;
    --rule-dash: rgba(255, 255, 255, 0.85);
  }
  html, body {
    margin: 0;
    padding: 0;
    width: 1200px;
    height: 685px;
    overflow: hidden;
    background: var(--card-light);
  }
  .card {
    position: relative;
    width: 1200px;
    height: 685px;
    overflow: hidden;
    background: var(--brand-purple);
    font-family: "Ubuntu", Arial, sans-serif;
  }
  .card-waves {
    position: absolute;
    inset: 0;
    width: 1200px;
    height: 685px;
  }
  .wave-top, .wave-bottom { fill: var(--card-light); }

  .brand-top {
    position: absolute;
    left: 796px;
    top: 86px;
    display: flex;
    align-items: center;
    gap: 16px;
    color: var(--brand-purple);
  }
  .brand-dot {
    width: 26px;
    height: 26px;
    border-radius: 50%;
    background: var(--brand-purple);
    flex: none;
  }
  .brand-name {
    font-size: 25px;
    line-height: 34px;
    font-weight: 400;
  }

  .contact-list {
    position: absolute;
    left: 80px;
    top: 236px;
    margin: 0;
    padding: 0;
    list-style: none;
  }
  .contact-item {
    position: relative;
    height: 81px;
    display: flex;
    align-items: center;
  }
  .contact-icon {
    width: 50px;
    height: 62px;
    flex: none;
  }
  .contact-text {
    margin-left: 44px;
    width: 462px;
    padding-bottom: 8px;
    border-bottom: 2px dashed var(--rule-dash);
    color: var(--card-white);
    white-space: nowrap;
  }
  .contact-owner { font-size: 27px; }
  .contact-email { font-size: 29px; }
  .contact-phone { font-size: 35px; }

  .brand-side {
    position: absolute;
    left: 808px;
    top: 312px;
    width: 300px;
    text-align: center;
    color: var(--card-white);
  }
  .brand-side-ring {
    display: block;
    width: 44px;
    height: 44px;
    margin: 0 auto 24px;
    border: 2px dashed var(--rule-dash);
    border-radius: 50%;
  }
  .brand-side .brand-name { font-size: 25px; line-height: 36px; }

  .social-list {
    position: absolute;
    left: 0;
    top: 620px;
    margin: 0;
    padding: 0;
    list-style: none;
  }
  .social-item {
    position: absolute;
    display: flex;
    align-items: center;
    gap: 14px;
    color: var(--brand-purple);
    font-size: 28px;
    white-space: nowrap;
  }
  .social-dot {
    width: 36px;
    height: 36px;
    border-radius: 50%;
    background: var(--brand-purple);
    flex: none;
  }
  .social-one { left: 36px; }
  .social-two { left: 404px; }
  .social-three { left: 748px; }
</style>
</head>
<body>
<main class="card">
  <svg class="card-waves" viewBox="0 0 1200 685" aria-hidden="true">
    <path class="wave-top" d="M486 0 C565 22 610 62 705 98 C805 136 890 176 1010 186 C1100 193 1160 196 1200 198 V0 Z"/>
    <path class="wave-bottom" d="M0 553 C190 600 380 592 600 566 C850 536 1040 512 1200 503 V685 H0 Z"/>
  </svg>

  <div class="brand-top">
    <span class="brand-dot"></span>
    <span class="brand-name">Skyward and<br>Engine Works</span>
  </div>

  <ul class="contact-list">
    <li class="contact-item">
      <svg class="contact-icon" viewBox="0 0 50 62" aria-hidden="true">
        <path d="M25 3 C25 3 5 27 5 39 A20 20 0 0 0 45 39 C45 27 25 3 25 3 Z" fill="none" stroke="#fff" stroke-width="2" stroke-dasharray="4 3"/>
        <rect x="19" y="30" width="12" height="19" rx="2" fill="none" stroke="#fff" stroke-width="2.4"/>
        <line x1="23" y1="45" x2="27" y2="45" stroke="#fff" stroke-width="2"/>
      </svg>
      <span class="contact-text contact-owner">Owner, Mr. “Dorian Vecksley”</span>
    </li>
    <li class="contact-item">
      <svg class="contact-icon" viewBox="0 0 50 62" aria-hidden="true">
        <path d="M25 3 C25 3 5 27 5 39 A20 20 0 0 0 45 39 C45 27 25 3 25 3 Z" fill="none" stroke="#fff" stroke-width="2" stroke-dasharray="4 3"/>
        <rect x="15" y="33" width="20" height="13" fill="#fff"/>
        <path d="M15 33 L25 41 L35 33" fill="none" stroke="#4b2b8f" stroke-width="1.8"/>
      </svg>
      <span class="contact-text contact-email">dorian-r-vecksley@quillmail.com.au</span>
    </li>
    <li class="contact-item">
      <svg class="contact-icon" viewBox="0 0 50 62" aria-hidden="true">
        <path d="M25 3 C25 3 5 27 5 39 A20 20 0 0 0 45 39 C45 27 25 3 25 3 Z" fill="none" stroke="#fff" stroke-width="2" stroke-dasharray="4 3"/>
        <circle cx="25" cy="39" r="10" fill="none" stroke="#fff" stroke-width="2"/>
        <ellipse cx="25" cy="39" rx="4.5" ry="10" fill="none" stroke="#fff" stroke-width="1.6"/>
        <line x1="15" y1="39" x2="35" y2="39" stroke="#fff" stroke-width="1.6"/>
      </svg>
      <span class="contact-text contact-phone">(Australia) 0471-593-064</span>
    </li>
  </ul>

  <div class="brand-side">
    <span class="brand-side-ring"></span>
    <span class="brand-name">Skyward and<br>Engine Works</span>
  </div>

  <ul class="social-list">
    <li class="social-item social-one"><span class="social-dot"></span>linkmesh.com/skyward</li>
    <li class="social-item social-two"><span class="social-dot"></span>chirpline.com/skyward</li>
    <li class="social-item social-three"><span class="social-dot"></span>vidcast.com/skyward</li>
  </ul>
</main>
</body>
</html>
```